Website for Brackley Fabrication & Construction Ltd

General Note to all.

1. Piling and gas works are separate areas of work and should not be put together.
- the marine section should really be the piling works and should have all the barges/water piles etc.
- the gas section should have the big silo looking thing

2. I would like to add in Specialist Onsite Labour and Management in the 'our services' section. The would include the Supervisors, Coded Welders, Site Fitters and Crane and Rig Crews etc.

3. I did like it how someone had use the BFC header logo as the top of the webpage with the individual tabs above and the website starting below. Please remove the VAT number and phone number from this section.

4. I also liked how one designer incorporate the orange line with spark (from the logo) as a page separator representing the welding part of the business

5. Add in a Mission Statement - To go above and beyond in to ensure our clients projects are delivered safely, ahead of schedule, in any environment for the benefit of not only our customers but also our employees and communities we work in.

6. Add in Business Objectives -BFC is on a mission to be one of the leading contractors in UK to supply All Site Labour - ranging from Site Management, fully Coded Welders, Site Fitters and Crane and Rig Crews.

7. I am happy for you to add in photos that are not ours for the thumbs nails for the our services. ie a colourful welding pics/cool tunnelling pic etc - just make sure I will not get done for copy write infringements

8. I would like a some type of 'contact us' field or 'request a consultation' section.

9. Please confirm if the webpages you create will be compatible for both desktop and mobile app and how difficult it will be to update personally once it is live.

10. You have all done very well and have thus far been very impressed with what you have produced. I gave a very vague brief as I was not entirely sure how you would go about making something with very little information. Some of the designs look very professional.

11. I'm not sure how once I choose the winning design how that then transfers over to my domain? Perhaps someone can help me with that? I will also be looking for a web hosting platform so feel free to provide this information.

After using Sketch hive for successful getting a professional logo for the company I'm giving the web design option a go.

I am looking for a professional website for the above civil construction company.

The company director has many years experience in Marine, tunnelling, conveyors, stadium construction gas and piling works including piling works for coal ports, bridges and tunnels.

The company currently provide 20+ skilled and experienced guys from all trades (supervisors, coded welders, fitters, crane drivers and crane supervisors, rigglers, slingers and piling operatives) on the Corran Flowpath project in London - London's new super sewer. Most of this work is off barges carrying cranes (upto 600T and drill rigs).

As we are looking to expand and get more subcontracts we need a web presence to say who we are and what we do.

I'll include the 2 company logos we currently use below

I have included an info doc with pics you may or may not use.

Target Market(s)

Mainly other large construction companies and potential subcontractors

Industry/Entity Type

Construction Company

Coding

Coded - Design and coding required

Font styles to use
Sans Serif

Colors
0655a3
f37122
ffffff

Requirements
Must have
• Few tabs
• Simple to use/update but still professional look
• The challenge will be making the website look professional with not much available content.
Should not have
• No residential house building

```html
<!DOCTYPE html>
<html lang="en">
<head>
<meta charset="utf-8">
<title>Brackley Fabrication &amp; Construction Ltd</title>
<link rel="stylesheet" href="https://fonts.googleapis.com/css2?family=Exo+2:wght@500;600;700&family=Questrial&display=swap">
<style>
:root{
  --blue:#0655a3;
  --navy:#123f73;
  --orange:#f37122;
  --white:#ffffff;
  --ink:#3d3d3d;
  --grey:#f2f2f2;
  --line:#dcdcdc;
}
*{box-sizing:border-box;margin:0;padding:0}
html,body{width:1200px;height:4380px;overflow:hidden}
body{position:relative;background:var(--white);font-family:"Questrial",sans-serif;color:var(--ink)}
.abs{position:absolute}
.head{font-family:"Exo 2",sans-serif;font-weight:700;letter-spacing:.5px}

/* top bar */
.topbar{top:0;left:0;width:1200px;height:35px;font-size:12px;color:#555}
.topbar .reg{left:112px;top:11px}
.topbar .mail{left:505px;top:11px}
.topbar .call{left:680px;top:11px}
.topbar svg{vertical-align:-3px;margin-right:6px}
.btn-consult-top{left:955px;top:3px;width:130px;height:28px;border:1.5px solid var(--orange);color:var(--orange);font-size:11px;font-weight:700;display:flex;align-items:center;justify-content:center;font-family:"Exo 2",sans-serif}

/* nav */
.nav{top:35px;left:0;width:1200px;height:115px;border-bottom:1px solid var(--line)}
.nav a{position:absolute;top:50px;font-family:"Exo 2",sans-serif;font-weight:600;font-size:14px;color:var(--navy);text-decoration:none}
.nav a.active{color:var(--orange)}
.nav a.active::after{content:"";position:absolute;left:-12px;right:-12px;bottom:-10px;height:2px;background:var(--orange)}
.brand{left:525px;top:-28px;width:150px;height:150px;border-radius:50%;background:var(--white);border:4px solid var(--navy);display:flex;flex-direction:column;align-items:center;justify-content:center;gap:2px}
.brand .mark{font-family:"Exo 2",sans-serif;font-weight:700;font-size:40px;color:var(--navy);line-height:1}
.brand .sub{font-family:"Exo 2",sans-serif;font-weight:700;font-size:9px;color:var(--navy);text-align:center;line-height:1.2}

/* hero */
.hero{top:152px;left:0;width:1200px;height:525px;background:linear-gradient(180deg,#c9ced3 0%,#8e9aa5 40%,#5d6670 62%,#3a3f44 82%,#1f2225 100%)}
.hero .photo-accent{left:360px;top:40px;width:260px;height:360px;background:linear-gradient(180deg,rgba(243,113,34,.0),rgba(243,113,34,.35));}
.hero-title{left:0;top:428px;width:1200px;text-align:center;color:var(--white);font-size:24px;line-height:34px;text-transform:uppercase}
.hero-title em{font-style:normal;color:var(--orange)}
.arrow{width:38px;height:38px;border-radius:50%;background:rgba(0,0,0,.35);display:flex;align-items:center;justify-content:center}

/* separators */
.spark{left:510px;width:180px;height:16px}

/* about */
.section-title{left:0;width:1200px;text-align:center;font-size:30px;color:var(--navy)}
.section-title em{font-style:normal;color:var(--orange)}
.about-text{left:210px;top:828px;width:780px;text-align:center;font-size:13px;line-height:21px;color:#444}
.about-text p{margin-bottom:14px}
.about-text .hl{color:var(--orange)}
.btn-navy{background:var(--navy);color:var(--white);font-size:13px;display:flex;align-items:center;justify-content:center;font-family:"Questrial",sans-serif}

/* mission */
.values{top:1168px;left:0;width:1200px;height:262px;background:linear-gradient(180deg,#ffffff 0%,#f0f0f0 100%)}
.notch{left:575px;top:1150px;width:0;height:0;border-left:25px solid transparent;border-right:25px solid transparent;border-bottom:18px solid #f8f8f8}
.value h3{font-family:"Exo 2",sans-serif;font-weight:700;font-size:20px;color:var(--navy);margin-bottom:12px}
.value h3 em{font-style:normal;color:var(--orange)}
.value p{font-size:12px;line-height:18px;color:#444}

/* services */
.services{top:1430px;left:0;width:1200px;height:565px;background:linear-gradient(135deg,#f58a3e 0%,#f37122 45%,#d95f15 100%)}
.services .intro{left:300px;top:142px;width:600px;text-align:center;color:var(--white);font-size:14px;line-height:22px}
.svc{top:210px;width:170px;text-align:center}
.svc .thumb{width:150px;height:150px;border-radius:50%;border:4px solid var(--white);margin:0 auto 16px}
.svc .label{font-family:"Exo 2",sans-serif;font-weight:700;color:var(--white);font-size:15px;line-height:20px;text-transform:uppercase}

/* projects */
.slide{left:114px;top:2160px;width:676px;height:600px;background:linear-gradient(180deg,#b7c7d6 0%,#9cb0bf 45%,#6f7d70 70%,#4a5257 100%)}
.slide .caption{left:0;bottom:0;width:676px;height:120px;background:rgba(20,24,30,.78);padding:22px 36px 0}
.slide .caption h4{font-family:"Exo 2",sans-serif;font-weight:600;color:var(--orange);font-size:16px;margin-bottom:12px}
.slide .caption p{color:var(--white);font-size:12px;line-height:18px}
.thumb-proj{left:800px;width:290px;height:145px}
.thumb-proj span{position:absolute;left:0;bottom:10px;width:100%;text-align:center;color:var(--white);font-size:12px;font-family:"Exo 2",sans-serif}

/* cta */
.cta{top:2905px;left:0;width:1200px;height:278px;background:linear-gradient(90deg,#2b2622 0%,#3d3631 50%,#4a3a2b 100%)}
.cta h2{position:absolute;left:115px;top:72px;font-family:"Exo 2",sans-serif;font-weight:700;font-size:30px;color:var(--white)}
.cta p{position:absolute;left:115px;top:118px;width:680px;font-size:24px;line-height:34px;color:var(--white)}
.btn-orange{left:885px;top:102px;width:200px;height:76px;background:var(--orange);color:var(--white);font-family:"Exo 2",sans-serif;font-weight:600;font-size:19px;line-height:24px;text-align:center;display:flex;align-items:center;justify-content:center}

/* partners */
.partner{top:3352px;width:150px;height:70px;display:flex;align-items:center;justify-content:center;gap:8px;font-family:"Exo 2",sans-serif;font-weight:700;font-size:18px;color:var(--navy)}
.partner i{width:12px;height:12px;background:var(--orange);display:inline-block}

/* map + footer */
.map{top:3504px;left:0;width:1200px;height:424px;background:linear-gradient(135deg,#eceee9 0%,#e3e6df 50%,#dfe6dc 100%)}
.footer{top:3927px;left:0;width:1200px;height:418px;background:var(--navy)}
.card-left{left:115px;top:3703px;width:485px;height:385px;background:var(--white)}
.card-right{left:600px;top:3703px;width:485px;height:385px;background:var(--orange);padding:30px 38px}
.card-right h3{font-family:"Exo 2",sans-serif;font-weight:700;font-size:26px;color:var(--white);margin-bottom:30px}
.field{position:absolute;color:var(--white);font-size:12px;border-bottom:1px solid rgba(255,255,255,.7);height:30px;padding-top:4px}
.follow{left:0;top:262px;width:485px;text-align:center;font-size:16px;color:var(--navy)}
.social{top:296px;width:34px;height:34px;border-radius:50%}
.foot-links{top:4140px;left:0;width:1200px;display:flex;justify-content:center;gap:70px;font-family:"Exo 2",sans-serif;font-weight:600;font-size:12px;color:var(--white)}
.foot-info{top:4180px;width:240px;text-align:center;color:var(--white);font-size:12px;line-height:18px}
.foot-info .ic{width:46px;height:46px;border:1.5px solid var(--white);border-radius:50%;margin:0 auto 10px;display:flex;align-items:center;justify-content:center}
.copyright{top:4345px;left:0;width:1200px;height:35px;background:var(--orange);color:var(--white);font-size:11px;display:flex;align-items:center;justify-content:center}
</style>
</head>
<body>

<!-- top bar -->
<div class="abs topbar">
  <span class="abs reg">Company Reg No: 10482273</span>
  <span class="abs mail"><svg width="14" height="12" viewBox="0 0 14 12"><path d="M0 6 14 0 10 12 7 8z" fill="#123f73"/></svg>Mail Us: info@bfc.com</span>
  <span class="abs call"><svg width="16" height="12" viewBox="0 0 16 12"><path d="M1 3c4-3 10-3 14 0l-2 3-3-1V3H6v2L3 6z M3 7h10v5H3z" fill="#123f73"/></svg>Call Now: 123-456-7890</span>
  <div class="abs btn-consult-top">REQUEST A CONSULTATION</div>
</div>

<!-- navigation -->
<nav class="abs nav">
  <a class="active" style="left:122px">HOME</a>
  <a style="left:243px">ABOUT US</a>
  <a style="left:392px">SERVICES</a>
  <div class="abs brand"><span class="mark">BFC</span><span class="sub">BRACKLEY FABRICATION<br>&amp; CONSTRUCTION</span></div>
  <a style="left:746px">GALLERY</a>
  <a style="left:870px">CLIENTS</a>
  <a style="left:990px">CONTACT US</a>
</nav>

<!-- hero -->
<section class="abs hero" role="img" aria-label="Photo of a piling barge with crane and welders on the river">
  <div class="abs photo-accent"></div>
  <div class="abs arrow" style="left:22px;top:245px"><svg width="12" height="14"><path d="M9 1 3 7l6 6" stroke="#fff" stroke-width="2" fill="none"/></svg></div>
  <div class="abs arrow" style="left:1140px;top:245px"><svg width="12" height="14"><path d="M3 1l6 6-6 6" stroke="#fff" stroke-width="2" fill="none"/></svg></div>
  <h1 class="abs hero-title head">Brackley Fabrication &amp; Construction has over <em>15 years experience</em><br>working in the civil construction industry</h1>
</section>

<!-- about -->
<h2 class="abs section-title head" style="top:748px"><em>ABOUT</em> BRACKLEY FABRICATION &amp; CONSTRUCTION</h2>
<svg class="abs spark" style="top:790px" viewBox="0 0 180 16"><line x1="0" y1="8" x2="180" y2="8" stroke="#f37122" stroke-width="2"/><circle cx="90" cy="8" r="6" fill="#f37122"/><path d="M90 0v16M82 8h16M84 2l12 12M96 2 84 14" stroke="#f37122" stroke-width="1"/></svg>
<div class="abs about-text">
  <p>Brackley Fabrication &amp; Construction has over <span class="hl">15 years experience working in the civil construction industry.</span> We are currently working on the Corran Flowpath project in London. We are subcontracted to Harlow Marsh Joint Venture and provide a highly skilled workforce across many of the Corran Flowpath sites.</p>
  <p>We have a strong history in the piling industry both in the UK and in Australia. Notable projects include working on Berth 7 and 10 Coal Terminal with Kestrel Civil and Wendle Bridge over the Aldery River for Ashvale Group in NSW Australia.</p>
  <p>Daniel Brackley was born and raised in South East London. After finishing school he completed a Welding and Fabrication apprenticeship with Corbet Welders and Corbet Civils.</p>
</div>
<div class="abs btn-navy" style="left:540px;top:1058px;width:120px;height:36px">Read More</div>

<!-- mission & objectives -->
<section class="abs values">
  <svg class="abs" style="left:112px;top:78px" width="90" height="90" viewBox="0 0 90 90"><path d="M45 4a41 41 0 1 0 41 41" stroke="#123f73" stroke-width="4" fill="none"/><path d="M86 45A41 41 0 0 0 45 4" stroke="#f37122" stroke-width="4" fill="none"/><circle cx="45" cy="45" r="22" fill="none" stroke="#123f73" stroke-width="3"/><circle cx="45" cy="45" r="12" fill="none" stroke="#f37122" stroke-width="3"/><circle cx="45" cy="45" r="4" fill="#123f73"/><path d="M45 45 66 24m0 0h-8m8 0v8" stroke="#123f73" stroke-width="3" fill="none"/></svg>
  <div class="abs value" style="left:250px;top:80px;width:200px">
    <h3><em>OUR</em> MISSION</h3>
    <p>To go above and beyond in to ensure our clients projects are delivered safely, ahead of schedule, in any environment for the benefit of not only our customers but also our employees and communities we work in.</p>
  </div>
  <svg class="abs" style="left:638px;top:78px" width="90" height="90" viewBox="0 0 90 90"><path d="M45 4a41 41 0 1 0 41 41" stroke="#123f73" stroke-width="4" fill="none"/><path d="M86 45A41 41 0 0 0 45 4" stroke="#f37122" stroke-width="4" fill="none"/><circle cx="45" cy="45" r="16" fill="none" stroke="#123f73" stroke-width="5" stroke-dasharray="6 4"/><circle cx="45" cy="45" r="7" fill="#f37122"/></svg>
  <div class="abs value" style="left:775px;top:80px;width:250px">
    <h3><em>BUSINESS</em> OBJECTIVES</h3>
    <p>BFC is on a mission to be one of the leading contractors in UK to supply All Site Labour - ranging from Site Management, fully Coded Welders, Site Fitters and Crane and Rig Crews.</p>
  </div>
</section>
<div class="abs notch"></div>

<!-- services -->
<section class="abs services" role="img" aria-label="Orange-toned photo of a construction site with workers">
  <h2 class="abs section-title head" style="top:62px;color:#fff">OUR SERVICES</h2>
  <svg class="abs spark" style="top:102px" viewBox="0 0 180 16"><line x1="0" y1="8" x2="180" y2="8" stroke="#fff" stroke-width="2"/><circle cx="90" cy="8" r="6" fill="#fff"/><path d="M90 0v16M82 8h16M84 2l12 12M96 2 84 14" stroke="#fff" stroke-width="1"/></svg>
  <p class="abs intro">Our Specialist Onsite Labour and Management include the Supervisors, Coded Welders, Site Fitters and Crane and Rig Crews etc.</p>
  <svg class="abs" style="left:70px;top:285px" width="14" height="20"><path d="M11 2 3 10l8 8" stroke="#fff" stroke-width="3" fill="none"/></svg>
  <svg class="abs" style="left:1110px;top:285px" width="14" height="20"><path d="M3 2l8 8-8 8" stroke="#fff" stroke-width="3" fill="none"/></svg>
  <div class="abs svc" style="left:105px"><div class="thumb" role="img" aria-label="Photo of a piling barge on water" style="background:linear-gradient(180deg,#8fa6b8,#5b6a72)"></div><div class="label">Marine and<br>Piling Works</div></div>
  <div class="abs svc" style="left:310px"><div class="thumb" role="img" aria-label="Photo of a tunnel boring section" style="background:linear-gradient(180deg,#6d6a66,#2f2d2b)"></div><div class="label">Tunnelling<br>Services</div></div>
  <div class="abs svc" style="left:515px"><div class="thumb" role="img" aria-label="Photo of bridge steelwork" style="background:linear-gradient(180deg,#c6cbd0,#7f8790)"></div><div class="label">Bridge<br>Construction</div></div>
  <div class="abs svc" style="left:720px"><div class="thumb" role="img" aria-label="Photo of stadium roof structure" style="background:linear-gradient(180deg,#d5d9dd,#8a9199)"></div><div class="label">Stadium<br>Construction</div></div>
  <div class="abs svc" style="left:925px"><div class="thumb" role="img" aria-label="Photo of site labour crew" style="background:linear-gradient(180deg,#e6e9ec,#a9b4bf)"></div><div class="label">Skilled Labour<br>Supply</div></div>
  <div class="abs btn-navy" style="left:495px;top:465px;width:210px;height:36px">Request A Consultation</div>
</section>

<!-- projects -->
<h2 class="abs section-title head" style="top:2065px">OUR PROJECTS</h2>
<svg class="abs spark" style="top:2106px" viewBox="0 0 180 16"><line x1="0" y1="8" x2="180" y2="8" stroke="#f37122" stroke-width="2"/><circle cx="90" cy="8" r="6" fill="#f37122"/><path d="M90 0v16M82 8h16M84 2l12 12M96 2 84 14" stroke="#f37122" stroke-width="1"/></svg>
<div class="abs slide" role="img" aria-label="Photo of a crawler crane on a river barge">
  <div class="abs arrow" style="left:-2px;top:280px;background:#fff"><svg width="12" height="14"><path d="M9 1 3 7l6 6" stroke="#333" stroke-width="2" fill="none"/></svg></div>
  <div class="abs arrow" style="left:640px;top:280px;background:#fff"><svg width="12" height="14"><path d="M3 1l6 6-6 6" stroke="#333" stroke-width="2" fill="none"/></svg></div>
  <div class="abs caption">
    <h4>Eastfield Line Extension - London</h4>
    <p>Lorem ipsum dolor sit amet, consectetuer adipiscing elit, sed diam nonummy nibh euismod tincidunt ut laoreet dolore magna aliquam erat volutpat. Ut wisi enim ad minim veniam.</p>
  </div>
</div>
<div class="abs thumb-proj" role="img" aria-label="Photo of a rail extension site" style="top:2160px;background:linear-gradient(180deg,#2d6aa8,#17406d)"><span style="top:50px;bottom:auto;font-size:17px">Eastfield Line Extension<br>- London</span></div>
<div class="abs thumb-proj" role="img" aria-label="Photo of a large silo tank" style="top:2313px;background:linear-gradient(180deg,#d8dadb,#8d9192)"><span>Gas Storage</span></div>
<div class="abs thumb-proj" role="img" aria-label="Photo of welding sparks" style="top:2466px;background:linear-gradient(135deg,#4a1c14,#b54a2a 55%,#2b1410)"><span>Riverside Arena - London</span></div>
<div class="abs thumb-proj" role="img" aria-label="Photo of a coal berth jetty" style="top:2619px;background:linear-gradient(180deg,#aebdc8,#5e6a72)"><span>Berth 7 &amp; 10 Coal Terminal</span></div>
<div class="abs btn-navy" style="left:540px;top:2805px;width:120px;height:36px">View All</div>

<!-- call to action -->
<section class="abs cta" role="img" aria-label="Dark photo of a tunnel interior">
  <h2>NEED CIVIL CONSTRUCTION?</h2>
  <p>Lorem ipsum dolor sit amet, consectetuer adipiscing elit, sed diam nonummy nibh euismod tincidunt ut laoreet dolore</p>
  <div class="abs btn-orange">REQUEST A<br>CONSULTATION</div>
</section>

<!-- partners -->
<h2 class="abs section-title head" style="top:3250px">WORKED WITH</h2>
<svg class="abs spark" style="top:3292px" viewBox="0 0 180 16"><line x1="0" y1="8" x2="180" y2="8" stroke="#f37122" stroke-width="2"/><circle cx="90" cy="8" r="6" fill="#f37122"/><path d="M90 0v16M82 8h16M84 2l12 12M96 2 84 14" stroke="#f37122" stroke-width="1"/></svg>
<div class="abs partner" style="left:105px;font-size:14px">Corran Flowpath</div>
<div class="abs partner" style="left:280px">Fennick</div>
<div class="abs partner" style="left:450px">Orvale</div>
<div class="abs partner" style="left:625px"><i></i>Marlow Crane</div>
<div class="abs partner" style="left:790px">Corbet</div>
<div class="abs partner" style="left:960px;font-size:16px">Halden Marine</div>

<!-- map & footer -->
<div class="abs map" role="img" aria-label="Street map showing the office location"></div>
<footer class="abs footer"></footer>

<div class="abs card-left">
  <div class="abs" style="left:162px;top:40px;width:160px;height:160px;border-radius:50%;border:4px solid var(--navy);display:flex;flex-direction:column;align-items:center;justify-content:center">
    <span class="head" style="font-size:44px;color:var(--navy);line-height:1">BFC</span>
    <span class="head" style="font-size:9px;color:var(--navy);text-align:center;line-height:1.3">BRACKLEY FABRICATION<br>&amp; CONSTRUCTION</span>
  </div>
  <div class="abs follow">Follow Us On</div>
  <span class="abs social" aria-label="Social link" style="left:160px;background:var(--navy)"></span>
  <span class="abs social" aria-label="Social link" style="left:203px;background:var(--blue)"></span>
  <span class="abs social" aria-label="Social link" style="left:246px;background:var(--navy)"></span>
  <span class="abs social" aria-label="Social link" style="left:289px;background:var(--orange)"></span>
</div>

<div class="abs card-right">
  <h3>QUICK INQUIRY</h3>
  <div class="field" style="left:38px;top:92px;width:190px">Name</div>
  <div class="field" style="left:258px;top:92px;width:190px">Email</div>
  <div class="field" style="left:38px;top:155px;width:190px">Phone</div>
  <div class="field" style="left:258px;top:155px;width:190px">Select Services <span style="float:right">&#9662;</span></div>
  <div class="field" style="left:38px;top:218px;width:410px;height:60px">Message</div>
  <div class="abs btn-navy" style="left:38px;top:310px;width:140px;height:32px;font-weight:700">SUBMIT NOW</div>
</div>

<nav class="abs foot-links"><span>HOME</span><span>ABOUT US</span><span>SERVICES</span><span>GALLERY</span><span>CONTACT US</span></nav>

<div class="abs foot-info" style="left:205px">
  <div class="ic"><svg width="16" height="22" viewBox="0 0 16 22"><path d="M8 1a7 7 0 0 1 7 7c0 5-7 13-7 13S1 13 1 8a7 7 0 0 1 7-7z" fill="none" stroke="#fff" stroke-width="1.6"/><circle cx="8" cy="8" r="2.5" fill="#fff"/></svg></div>
  Loren 123, Dolor sit amet,<br>hendrerit in vulputate, CA 123456
</div>
<div class="abs foot-info" style="left:490px">
  <div class="ic"><svg width="20" height="20" viewBox="0 0 20 20"><path d="M4 1h4l2 5-3 2a11 11 0 0 0 5 5l2-3 5 2v4c0 2-2 3-3 3C8 19 1 12 1 4c0-1 1-3 3-3z" fill="none" stroke="#fff" stroke-width="1.6"/></svg></div>
  Call:<br>123-456-7890
</div>
<div class="abs foot-info" style="left:760px">
  <div class="ic"><svg width="22" height="16" viewBox="0 0 22 16"><rect x="1" y="1" width="20" height="14" fill="none" stroke="#fff" stroke-width="1.6"/><path d="M1 1l10 8 10-8" fill="none" stroke="#fff" stroke-width="1.6"/></svg></div>
  Email:<br>info@brackleyconstruction.com
</div>

<div class="abs copyright">Copyright © 2018 Brackley Fabrication &amp; Construction. All Rights Reserved</div>

</body>
</html>
```